Rack Card for IV Infusion Vitamin Supplement bar

We need a very eye catching rack card so that customers would instantly know it is for IV vitamin infusions. We have our previous rack card (pdf) as an example that did not bring in any clients as an example as well as another one that we did not like too much. The bar is for people to feel better with hydration and vitamins.

Target Market(s)

Anyone

Industry/Entity Type

Healthcare

Requirements
Must have
• Logo on rack card
Should not have
• Not pink other than the logo

```html
<!DOCTYPE html>
<html lang="en">
<head>
<meta charset="utf-8">
<title>Bloom Health &amp; Wellness – Rack Card</title>
<link href="https://fonts.googleapis.com/css2?family=Montserrat:wght@400;600;700;800&family=Nunito+Sans:wght@400;600&display=swap" rel="stylesheet">
<style>
  :root {
    --page-bg: #d9d4d4;
    --card-white: #ffffff;
    --sun-orange: #f8a51f;
    --forest: #0d4a3f;
    --teal-heading: #2e6b5e;
    --accent-orange: #f4a11a;
    --peach-light: #f7d2b8;
    --peach-deep: #e9a67c;
    --body-text: #2f2a24;
    --white: #ffffff;
  }
  * { box-sizing: border-box; margin: 0; padding: 0; }
  html, body { width: 1182px; height: 1200px; overflow: hidden; }
  body {
    background: var(--page-bg);
    position: relative;
    font-family: "Nunito Sans", Arial, sans-serif;
  }
  .card {
    position: absolute;
    top: 51px;
    width: 508px;
    height: 1106px;
    overflow: hidden;
  }
  .card--front { left: 47px; background: var(--card-white); }
  .card--back { left: 615px; background: var(--sun-orange); }

  /* Brand block */
  .brand {
    position: absolute;
    text-align: center;
    font-family: "Montserrat", Arial, sans-serif;
    color: var(--forest);
    font-weight: 700;
  }
  .front-brand { top: 75px; left: 0; right: 0; }
  .front-brand .brand-mark {
    width: 58px; height: 58px; border-radius: 50%;
    background: var(--forest);
    margin: 0 auto 18px;
  }
  .front-brand .brand-name { font-size: 62px; letter-spacing: 12px; line-height: 1; padding-left: 12px; }
  .front-brand .brand-tag { font-size: 15px; letter-spacing: 8px; margin-top: 6px; padding-left: 8px; }

  .front-title {
    position: absolute;
    top: 268px; left: 0; right: 0;
    text-align: center;
    font-family: "Montserrat", Arial, sans-serif;
    font-weight: 800;
    font-size: 31px;
    letter-spacing: 3px;
    line-height: 42px;
    color: var(--teal-heading);
  }
  .front-title .amp { color: var(--accent-orange); }

  .front-photo {
    position: absolute;
    top: 384px; left: 0;
    width: 508px; height: 600px;
    background: radial-gradient(ellipse at 50% 55%, var(--peach-light) 0%, var(--peach-deep) 100%);
  }

  /* Bottom bands */
  .book-band {
    position: absolute;
    left: 0; bottom: 0;
    width: 508px; height: 122px;
    background: var(--forest);
    color: var(--white);
    text-align: center;
  }
  .book-line {
    font-family: "Montserrat", Arial, sans-serif;
    font-weight: 800;
    font-size: 32px;
    letter-spacing: 1.8px;
    margin-top: 13px;
    line-height: 38px;
  }
  .book-line .book-cta { color: var(--accent-orange); margin-right: 10px; }
  .band-info {
    font-family: "Montserrat", Arial, sans-serif;
    font-size: 19px;
    line-height: 28px;
    font-weight: 600;
  }
  .band-info--light { font-weight: 400; }
  .band-info svg { vertical-align: -3px; margin-right: 6px; }

  /* Back */
  .back-brand { top: 45px; right: 37px; width: 135px; }
  .back-brand .brand-mark {
    width: 34px; height: 34px; border-radius: 50%;
    background: var(--forest);
    margin: 0 auto 12px;
  }
  .back-brand .brand-name { font-size: 30px; letter-spacing: 5px; line-height: 1; padding-left: 5px; }
  .back-brand .brand-tag { font-size: 7px; letter-spacing: 3.2px; margin-top: 4px; }

  .menu {
    position: absolute;
    top: 106px; left: 38px;
    width: 440px;
  }
  .menu-heading {
    font-family: "Montserrat", Arial, sans-serif;
    font-weight: 800;
    font-size: 22px;
    letter-spacing: 1px;
    color: var(--forest);
    line-height: 28px;
    margin-bottom: 1px;
  }
  .menu-heading--addons { margin-top: 26px; }
  .menu-item { margin-bottom: 4px; }
  .item-name {
    font-family: "Montserrat", Arial, sans-serif;
    font-weight: 800;
    font-size: 14.5px;
    color: var(--white);
    line-height: 19px;
    letter-spacing: 0.2px;
    white-space: nowrap;
  }
  .item-name::before { content: "> "; color: var(--forest); }
  .item-desc {
    font-size: 14px;
    line-height: 18.3px;
    color: var(--body-text);
    padding-left: 14px;
    white-space: nowrap;
  }
</style>
</head>
<body>

<section class="card card--front">
  <div class="brand front-brand">
    <div class="brand-mark"></div>
    <div class="brand-name">BLOOM</div>
    <div class="brand-tag">HEALTH &amp; WELLNESS</div>
  </div>
  <h1 class="front-title">VITAMIN INFUSIONS<br><span class="amp">&amp;</span> INJECTIONS</h1>
  <div class="front-photo" role="img" aria-label="Photo of a smiling woman holding an orange slice over one eye"></div>
  <footer class="book-band">
    <div class="book-line"><span class="book-cta">BOOK NOW</span>555-014-2290</div>
    <div class="band-info band-info--light">
      <svg width="14" height="18" viewBox="0 0 14 18" aria-hidden="true"><path d="M7 1a6 6 0 0 0-6 6c0 4.5 6 10 6 10s6-5.5 6-10a6 6 0 0 0-6-6z" fill="none" stroke="#fff" stroke-width="1.8"/><circle cx="7" cy="7" r="2.2" fill="#fff"/></svg>1420 N. Elm St., STE 2B Riverton
    </div>
    <div class="band-info band-info--light">
      <svg width="17" height="17" viewBox="0 0 18 18" aria-hidden="true"><g fill="none" stroke="#fff" stroke-width="1.3"><circle cx="9" cy="9" r="7.5"/><ellipse cx="9" cy="9" rx="3.3" ry="7.5"/><path d="M1.5 9h15M2.8 5h12.4M2.8 13h12.4"/></g></svg>www.bloomtotalhealth.com
    </div>
  </footer>
</section>

<section class="card card--back">
  <div class="brand back-brand">
    <div class="brand-mark"></div>
    <div class="brand-name">BLOOM</div>
    <div class="brand-tag">HEALTH &amp; WELLNESS</div>
  </div>

  <div class="menu">
    <h2 class="menu-heading">PREMIUM INFUSIONS</h2>
    <div class="menu-item"><div class="item-name">BLOOM COCKTAIL</div><p class="item-desc">Reduce stress, fatigue, and boost your energy. Bloom client<br>favorite! (IV fluids, Vitamin C, B-complex, B12, and electrolytes)</p></div>
    <div class="menu-item"><div class="item-name">IMMUNE SUPPORT</div><p class="item-desc">Protect the immune system when risk of illness is high. Great<br>for pre, post-travel (IV fluids, Vitamin C, B-complex, and Zinc)</p></div>
    <div class="menu-item"><div class="item-name">THE GLOW</div><p class="item-desc">Give a glowing boost to skin and hair from inside out. (IV fluids,<br>Glutathione, Vitamin B-complex, and Biotin)</p></div>
    <div class="menu-item"><div class="item-name">SPORTS RECOVERY</div><p class="item-desc">Recover fast from illness, exhaustion, and workouts. (IV fluids,<br>B-complex, B12, and amino acids, and electrolytes)</p></div>
    <div class="menu-item"><div class="item-name">ENERGIZED</div><p class="item-desc">Boost metabolism, burn fat easier, and feel energized. (IV<br>fluids, B-complex, and amino acid blend)</p></div>
    <div class="menu-item"><div class="item-name">BRAIN POWER</div><p class="item-desc">Support overall brain function, increase memory recall and<br>improve certain aspects of learning. (IV fluids, B6, alpha lipoic<br>acid, and taurine)</p></div>
    <div class="menu-item"><div class="item-name">THE JETLAG DRIP</div></div>
    <div class="menu-item"><div class="item-name">THE MIGRAINE / PMS DRIP</div></div>
    <div class="menu-item"><div class="item-name">THE HANGOVER DRIP</div></div>
    <div class="menu-item"><div class="item-name">NAD+ 125G/ 250G/ 500G DRIP</div><p class="item-desc">Enhance your cognitive health and help reverse aging.<br>Promotes cell regeneration. Can aid mental clarity, better sleep,<br>and energy.</p></div>
    <div class="menu-item"><div class="item-name">HIGH DOSE VITAMIN C</div><p class="item-desc">*Medical clearance required</p></div>

    <h2 class="menu-heading menu-heading--addons">INFUSIONS ADD-ONS</h2>
    <div class="menu-item"><div class="item-name">GLUTATHIONE</div><p class="item-desc">*A powerful natural antioxidant to help Detox</p></div>
    <div class="menu-item"><div class="item-name">ADDITIONAL VITAMIN C</div></div>
    <div class="menu-item"><div class="item-name">ADDITIONAL ZINC</div></div>
    <div class="menu-item"><div class="item-name">ADDITIONAL MAGNESIUM</div></div>
    <div class="menu-item"><div class="item-name">ANTI- INFLAMMATION MEDICATION</div></div>
    <div class="menu-item"><div class="item-name">ANTI-NAUSEA MEDICATION</div></div>
    <div class="menu-item"><div class="item-name">VITAMIN D SHOT</div></div>
    <div class="menu-item"><div class="item-name">VITAMIN B12 SHOT</div></div>
  </div>

  <footer class="book-band">
    <div class="book-line"><span class="book-cta">BOOK NOW</span>555-014-2290</div>
    <div class="band-info">BY APPOINTMENT ONLY</div>
    <div class="band-info band-info--light">(including weekends)</div>
  </footer>
</section>

</body>
</html>
```